hi all

Im after a new age looking business card with my company logo on it

must include these details, I would like the PH and Email to be symbols

If the colours used for card could be kept within the colours used in logo that I have supplied that would be great, if another colour is to be used dark grey would be ok. no light bulbs etc thanks

Details below to be incorporated on card

Damian Holloway

Lic E871302

PH 0219647381

E info@brightvaleelectrical.example.nz

Domestic Commercial Industrial Electricians

```html
<!DOCTYPE html>
<html lang="en">
<head>
<meta charset="utf-8">
<title>Brightvale Electrical – Business Card</title>
<link rel="stylesheet" href="https://fonts.googleapis.com/css2?family=Lato:wght@400;700;900&display=swap">
<style>
  :root {
    --stage: #3a3b3e;
    --card: #141417;
    --brand-blue: #1f7fd0;
    --ink-white: #f4f4f6;
    --ghost: #1e1e22;
    --ghost-line: #2a2a2f;
  }
  * { margin: 0; padding: 0; box-sizing: border-box; }
  html, body {
    width: 1200px; height: 900px; overflow: hidden;
    background: var(--stage);
    font-family: "Lato", sans-serif;
  }
  .stage {
    position: relative; width: 1200px; height: 900px;
    display: flex; flex-direction: column; align-items: center; justify-content: center; gap: 44px;
  }
  .card {
    position: relative; width: 680px; height: 388px;
    background: var(--card);
    border-radius: 30px;
    overflow: hidden;
    box-shadow: 0 14px 34px rgba(0,0,0,.45);
  }

  /* Front side */
  .front-ghost-ring {
    position: absolute; left: 36px; top: 40px; width: 340px; height: 300px;
    border-radius: 50%;
    border: 9px solid var(--ghost-line);
    background: var(--ghost);
  }
  .front-wordmark {
    position: absolute; right: 44px; top: 150px;
    color: var(--brand-blue); font-weight: 900; text-transform: uppercase;
    line-height: 1; white-space: nowrap;
  }
  .front-wordmark .word-main { display: block; font-size: 44px; letter-spacing: 1px; }
  .front-wordmark .word-sub { display: block; font-size: 16px; letter-spacing: 6px; margin-top: 6px; text-align: right; color: var(--ink-white); }

  /* Back side */
  .back-ghost-ring {
    position: absolute; right: 40px; top: 30px; width: 210px; height: 170px;
    border-radius: 50%;
    border: 6px solid var(--ghost-line);
    background: var(--ghost);
  }
  .brand-lockup {
    position: absolute; left: 48px; top: 42px;
    display: flex; align-items: center; gap: 14px;
  }
  .brand-dot {
    width: 56px; height: 56px; border-radius: 50%;
    background: var(--brand-blue);
  }
  .brand-name {
    color: var(--brand-blue); font-weight: 900; text-transform: uppercase; line-height: 1; white-space: nowrap;
  }
  .brand-name .word-main { display: block; font-size: 34px; letter-spacing: 1px; }
  .brand-name .word-sub { display: block; font-size: 13px; letter-spacing: 5px; margin-top: 4px; text-align: right; color: var(--ink-white); }

  .holder-name {
    position: absolute; left: 110px; top: 168px;
    font-size: 36px; font-weight: 900; letter-spacing: -.5px; white-space: nowrap;
  }
  .holder-name .first { color: var(--brand-blue); }
  .holder-name .last { color: var(--ink-white); }
  .name-rule {
    position: absolute; left: 112px; top: 224px; width: 40px; height: 2px;
    background: var(--brand-blue);
  }
  .contact-list {
    position: absolute; left: 110px; top: 240px; list-style: none;
    color: var(--ink-white); font-size: 19px;
  }
  .contact-list li { display: flex; align-items: center; gap: 14px; height: 32px; white-space: nowrap; }
  .contact-list svg { width: 20px; height: 20px; flex: none; }
  .services {
    position: absolute; left: 110px; top: 320px;
    color: var(--ink-white); font-size: 19px; white-space: nowrap;
  }
  .licence {
    position: absolute; right: 46px; top: 254px;
    color: var(--brand-blue); font-size: 19px; white-space: nowrap;
  }
</style>
</head>
<body>
<main class="stage">
  <section class="card card-front" aria-label="Card front">
    <div class="front-ghost-ring" aria-hidden="true"></div>
    <p class="front-wordmark"><span class="word-main">Brightvale</span><span class="word-sub">Electrical</span></p>
  </section>

  <section class="card card-back" aria-label="Card back">
    <div class="back-ghost-ring" aria-hidden="true"></div>
    <div class="brand-lockup">
      <span class="brand-dot" aria-hidden="true"></span>
      <p class="brand-name"><span class="word-main">Brightvale</span><span class="word-sub">Electrical</span></p>
    </div>

    <h1 class="holder-name"><span class="first">Damian</span> <span class="last">Holloway</span></h1>
    <div class="name-rule" aria-hidden="true"></div>

    <ul class="contact-list">
      <li>
        <svg viewBox="0 0 24 24" aria-label="Phone"><path fill="var(--brand-blue)" d="M6.6 10.8a15.1 15.1 0 0 0 6.6 6.6l2.2-2.2a1 1 0 0 1 1-.25 11.4 11.4 0 0 0 3.6.57 1 1 0 0 1 1 1V20a1 1 0 0 1-1 1A17 17 0 0 1 3 4a1 1 0 0 1 1-1h3.5a1 1 0 0 1 1 1c0 1.25.2 2.45.57 3.57a1 1 0 0 1-.25 1z"/></svg>
        <span>021 964 7381</span>
      </li>
      <li>
        <svg viewBox="0 0 24 24" aria-label="Email"><path fill="var(--brand-blue)" d="M2 5h20v14H2z"/><path fill="none" stroke="var(--card)" stroke-width="1.6" d="M2 5l10 8 10-8M2 19l7-7M22 19l-7-7"/></svg>
        <span>info@brightvaleelectrical.example.nz</span>
      </li>
    </ul>
    <p class="services">Domestic Commercial Industrial Electricians</p>
    <p class="licence">Lic E871302</p>
  </section>
</main>
</body>
</html>
```